Business Card Design Project

double sided, embossed, name & logo on front font sonsie one, back Name Marisol Venkamp, mobile 0468201934, Phone 73519086,
email marisol@brightspanservices.com, use sysbols on the back for example an envelope for email, a telephone for phone number etc.symbol slate grey writing navy blue

Industry/Entity Type

Business

```html
<!DOCTYPE html>
<html lang="en">
<head>
<meta charset="utf-8">
<title>Brightspan Services – Business Card Front</title>
<link href="https://fonts.googleapis.com/css2?family=Sonsie+One&display=swap" rel="stylesheet">
<style>
  :root {
    --navy: #304c76;
    --sky: #0aaeea;
    --sky-light: #8fd3f2;
    --page: #ffffff;
    --white: #ffffff;
  }
  * { margin: 0; padding: 0; box-sizing: border-box; }
  html, body {
    width: 1200px;
    height: 1000px;
    overflow: hidden;
    background: var(--page);
  }
  .card {
    position: absolute;
    left: 85px;
    top: 165px;
    width: 1050px;
    height: 600px;
    background: var(--white);
    overflow: hidden;
  }
  .card__art {
    position: absolute;
    inset: 0;
    width: 100%;
    height: 100%;
  }
  .card__brand {
    position: absolute;
    left: 0;
    right: 0;
    top: 238px;
    display: flex;
    justify-content: center;
    align-items: center;
    gap: 18px;
    font-family: "Sonsie One", cursive;
    font-weight: 400;
    font-size: 50px;
    line-height: 1;
    color: var(--navy);
    white-space: nowrap;
  }
  .card__brand-mark {
    flex: none;
    width: 84px;
    height: 84px;
    border-radius: 50%;
    background: var(--navy);
  }
  .card__name {
    position: absolute;
    left: 0;
    right: 0;
    top: 342px;
    text-align: center;
    font-family: "Sonsie One", cursive;
    font-size: 32px;
    line-height: 1;
    color: var(--navy);
    white-space: nowrap;
    text-shadow: 0 0 10px rgba(255,255,255,0.9), 0 0 4px rgba(255,255,255,0.9);
  }
  .sparkle {
    position: absolute;
    border-radius: 50%;
    background: radial-gradient(circle, rgba(255,255,255,1) 0%, rgba(255,255,255,0.6) 30%, rgba(255,255,255,0) 70%);
  }
  .sparkle--left { left: 70px; top: 165px; width: 130px; height: 150px; }
  .sparkle--right { left: 855px; top: 485px; width: 90px; height: 95px; }
</style>
</head>
<body>
  <section class="card" aria-label="Brightspan Services business card, front">
    <svg class="card__art" viewBox="0 0 1050 600" preserveAspectRatio="none" aria-hidden="true">
      <defs>
        <linearGradient id="upperSwoosh" x1="0" y1="0" x2="1" y2="0">
          <stop offset="0" stop-color="#1fa3dd"/>
          <stop offset="0.15" stop-color="#8fd3f2"/>
          <stop offset="0.45" stop-color="#00aeef"/>
          <stop offset="0.75" stop-color="#6fd0f5"/>
          <stop offset="1" stop-color="#ffffff"/>
        </linearGradient>
        <linearGradient id="midWash" x1="0" y1="0" x2="1" y2="0">
          <stop offset="0" stop-color="#6cc3ea"/>
          <stop offset="0.5" stop-color="#d6eef9"/>
          <stop offset="1" stop-color="#ffffff"/>
        </linearGradient>
        <linearGradient id="lowerSwoosh" x1="0" y1="0" x2="1" y2="0">
          <stop offset="0" stop-color="#304c76"/>
          <stop offset="0.3" stop-color="#1a86c4"/>
          <stop offset="0.5" stop-color="#00aeef"/>
          <stop offset="0.75" stop-color="#8fdcf7"/>
          <stop offset="1" stop-color="#ffffff"/>
        </linearGradient>
      </defs>
      <rect class="band-top" x="0" y="0" width="1050" height="113" fill="var(--navy)"/>
      <rect x="0" y="113" width="1050" height="376" fill="url(#midWash)"/>
      <path d="M225 113 Q560 225 1050 217 V113 Z" fill="url(#upperSwoosh)"/>
      <path d="M0 382 Q420 470 1050 340 V360 Q880 440 725 489 H0 Z" fill="url(#lowerSwoosh)"/>
      <rect class="band-bottom" x="0" y="489" width="1050" height="111" fill="var(--navy)"/>
    </svg>
    <div class="sparkle sparkle--left" role="img" aria-label="White sparkle glint"></div>
    <div class="sparkle sparkle--right" role="img" aria-label="White sparkle glint"></div>
    <h1 class="card__brand">Brightspan Services<span class="card__brand-mark"></span></h1>
    <p class="card__name">Marisol Venkamp</p>
  </section>
</body>
</html>
```